Residential Construction Company needs flyer designed.

We need a flyer design for a residential Rain Gutter and Screen room company. We have over 50 years in the remodeling industry and service all of Middle Georgia. We want the brochure to highlight our wonderful managerial staff to our great instillation crews. We also want to showcase the high-quality products that we use, gutter, leaf protection, screen rooms and sunrooms and the quality craftsmanship homeowners will receive when they choose to go with our company.

```html
<!DOCTYPE html>
<html lang="en">
<head>
<meta charset="utf-8">
<title>Harlow Gutters &amp; Exteriors – Residential Flyer</title>
<link href="https://fonts.googleapis.com/css2?family=Bebas+Neue&family=Montserrat:wght@300;400;500;600;700;800&family=Poppins:wght@400;500;600;700&display=swap" rel="stylesheet">
<style>
:root{
  --stage:#8c8c8c;
  --navy:#2a2470;
  --purple-deep:#24185a;
  --purple:#3b2a86;
  --teal:#17a797;
  --blue:#2479d0;
  --blue-btn:#2a7fd4;
  --ink:#1f1d3a;
  --white:#ffffff;
  --gold:#f2b51d;
  --pin:#d83a45;
}
*{box-sizing:border-box;margin:0;padding:0}
html,body{width:1200px;height:2382px;overflow:hidden;background:var(--stage)}
h1,h2{font-weight:inherit}
.flyer{position:absolute;left:50px;top:480px;width:1100px;height:1422px;overflow:hidden;
  background:linear-gradient(180deg,#eef0f4 0%,#f7f8fa 60%,#eceef2 100%);
  box-shadow:0 20px 40px rgba(0,0,0,.35);font-family:"Poppins",sans-serif;color:var(--ink)}
.abs{position:absolute}

/* header */
.header{position:absolute;left:0;top:0;width:1100px;height:475px;
  background:linear-gradient(90deg,var(--purple-deep) 0%,var(--purple) 100%);
  clip-path:polygon(0 0,100% 0,100% 475px,500px 475px,480px 459px,0 459px)}
.header-photo{position:absolute;left:497px;top:0;width:603px;height:475px;
  background:linear-gradient(90deg,rgba(50,35,120,1) 0%,rgba(50,35,120,.55) 25%,rgba(50,70,80,.2) 60%),
  linear-gradient(180deg,#3f5a66 0%,#2c3e48 55%,#8d9596 80%,#3a3a5a 100%)}
.tag-residential{left:0;top:51px;width:320px;height:43px;background:var(--teal);
  border-radius:0 10px 10px 0;color:var(--white);font-family:"Montserrat",sans-serif;font-weight:700;
  font-size:26px;letter-spacing:6px;padding-left:49px;line-height:43px;white-space:nowrap}
.title-line1{left:46px;top:112px;font-family:"Bebas Neue",sans-serif;font-size:84px;line-height:80px;color:var(--white);letter-spacing:.5px;white-space:nowrap}
.title-line2{left:46px;top:186px;font-family:"Montserrat",sans-serif;font-weight:800;font-size:62px;line-height:64px;color:var(--blue);white-space:nowrap}
.title-line3{left:46px;top:244px;font-family:"Montserrat",sans-serif;font-weight:400;font-size:64px;line-height:64px;color:var(--white);white-space:nowrap}
.mission{left:56px;top:332px;width:510px;border-left:4px solid var(--teal);padding-left:15px;
  color:var(--white);font-family:"Montserrat",sans-serif;font-weight:500;font-size:18.5px;line-height:21.8px}

/* services */
.section-title{font-family:"Montserrat",sans-serif;font-size:34px;font-weight:400;color:var(--ink);line-height:38px;white-space:nowrap}
.section-title b{font-weight:700;color:var(--navy)}
.service-title{left:49px;top:506px}
.service-rule{left:295px;top:529px;width:215px;height:2px;background:var(--navy)}
.house-photo{left:-120px;top:566px;width:526px;height:526px;border-radius:50%;border:5px solid var(--blue);
  background:linear-gradient(180deg,#8fb4d8 0%,#d6cfc2 30%,#8a6a55 55%,#5d6b45 78%,#7bb04a 100%)}
.service-item{display:flex;align-items:center;gap:10px}
.service-icon{width:70px;height:70px;border-radius:50%;background:var(--navy);border:4px solid var(--teal);
  box-shadow:0 0 0 4px var(--white);display:flex;align-items:center;justify-content:center;flex:none}
.service-label{font-family:"Montserrat",sans-serif;font-size:19.5px;line-height:23px;color:var(--ink);font-weight:500;white-space:nowrap}

/* specialties */
.spec-intro{left:569px;top:517px;font-family:"Poppins",sans-serif;font-weight:600;font-size:19.5px;line-height:26px;color:var(--ink);white-space:nowrap}
.spec-intro span{color:var(--blue);font-weight:700}
.spec-btn{height:48px;color:var(--white);font-family:"Poppins",sans-serif;font-weight:500;font-size:16px;line-height:18px;
  padding:5px 14px;display:flex;align-items:center;border-radius:2px}
.spec-btn.blue{background:var(--blue-btn)}
.spec-btn.teal{background:var(--teal)}
.products-title{left:569px;top:720px;font-family:"Poppins",sans-serif;font-weight:400;font-size:28px;line-height:30px;color:var(--ink);white-space:nowrap}
.products-title b{color:var(--navy);font-weight:700}
.product-card{width:236px;height:148px;border:3px solid var(--navy);background:var(--navy);overflow:hidden}
.product-photo{width:100%;height:108px}
.product-name{height:34px;color:var(--white);font-weight:600;font-size:18px;text-align:center;line-height:34px}
.craft-note{left:571px;top:1113px;width:480px;font-size:17.5px;line-height:22px;color:var(--ink)}
.craft-note b{font-weight:600}

/* bands */
.band{top:1178px;height:86px;display:flex;align-items:center;color:var(--white);font-family:"Montserrat",sans-serif;font-size:24px;line-height:28px}
.band-years{left:49px;width:507px;background:var(--navy);padding-left:123px}
.band-area{left:563px;width:483px;background:var(--blue-btn);padding-left:95px}
.band b{font-weight:800}

/* contact */
.brand-name{left:49px;top:1296px;width:270px;font-family:"Montserrat",sans-serif;font-weight:800;font-size:22px;line-height:26px;color:var(--navy);
  display:flex;align-items:center;gap:10px}
.brand-mark{width:20px;height:20px;background:var(--navy);flex:none}
.touch-title{left:354px;top:1280px;font-family:"Poppins",sans-serif;font-weight:400;font-size:31px;line-height:40px;color:var(--ink);white-space:nowrap}
.touch-title b{color:var(--navy);font-weight:700}
.touch-rule{left:715px;top:1305px;width:331px;height:2px;background:var(--navy)}
.phone{left:354px;top:1328px;display:flex;align-items:center;gap:8px;font-family:"Poppins",sans-serif;font-weight:700;font-size:30px;line-height:40px;color:var(--ink);white-space:nowrap}
.contact-lines{left:645px;top:1328px;font-size:17px;line-height:25px;font-weight:500;color:var(--ink);white-space:nowrap}
.contact-lines div{display:flex;align-items:center;gap:8px}
</style>
</head>
<body>
<main class="flyer">
  <section class="header">
    <div class="header-photo" role="img" aria-label="Photo of a gloved worker clearing leaves from a roof gutter"></div>
  </section>
  <div class="abs tag-residential">RESIDENTIAL</div>
  <h1>
    <span class="abs title-line1">RAIN GUTTER AND</span>
    <span class="abs title-line2">SCREEN ROOM</span>
    <span class="abs title-line3">COMPANY</span>
  </h1>
  <p class="abs mission">Our mission is to provide each customer with an excellent product, superior service and quality workmanship. We take great pride in our honesty, integrity and genuinely strive to exceed the expectations of every customer.</p>

  <h2 class="abs section-title service-title">OUR <b>SERVICE</b></h2>
  <div class="abs service-rule"></div>
  <div class="abs house-photo" role="img" aria-label="Photo of a two-storey brick house with a front porch and lawn"></div>

  <div class="abs service-item" style="left:212px;top:571px">
    <div class="service-icon"><svg width="36" height="36" viewBox="0 0 36 36" fill="none" stroke="#fff" stroke-width="2.2"><path d="M6 12h24l-4 10H10z"/><path d="M12 26v4M18 26v6M24 26v4"/></svg></div>
    <div class="service-label" style="margin-top:-28px">Gutter<br>Cleaning</div>
  </div>
  <div class="abs service-item" style="left:283px;top:651px">
    <div class="service-icon"><svg width="36" height="36" viewBox="0 0 36 36" fill="none" stroke="#fff" stroke-width="2.2"><path d="M5 10h26v8a8 8 0 0 1-8 8H13a8 8 0 0 1-8-8z"/><path d="M12 18h12"/></svg></div>
    <div class="service-label" style="margin-top:-28px">Gutter<br>Protection</div>
  </div>
  <div class="abs service-item" style="left:323px;top:740px">
    <div class="service-icon"><svg width="34" height="34" viewBox="0 0 34 34" fill="none" stroke="#fff" stroke-width="2.2"><rect x="5" y="5" width="24" height="24"/><path d="M17 5v24M5 17h24"/></svg></div>
    <div class="service-label" style="margin-top:-20px">Vinyl Film<br>Windows</div>
  </div>
  <div class="abs service-item" style="left:326px;top:846px">
    <div class="service-icon"><svg width="34" height="34" viewBox="0 0 34 34" fill="none" stroke="#fff" stroke-width="2.2"><path d="M8 6v12a8 8 0 0 0 8 8h12"/><path d="M13 6v11a4 4 0 0 0 4 4h11"/></svg></div>
    <div class="service-label" style="margin-top:-22px">Gutter<br>Systems</div>
  </div>
  <div class="abs service-item" style="left:291px;top:945px">
    <div class="service-icon"><svg width="36" height="36" viewBox="0 0 36 36" fill="none" stroke="#fff" stroke-width="2.2"><path d="M4 12h28M6 12V6h24v6"/><path d="M8 12v18M28 12v18M14 18h8v12h-8z"/></svg></div>
    <div class="service-label" style="margin-top:10px">Patio<br>Covers</div>
  </div>
  <div class="abs service-item" style="left:218px;top:1022px">
    <div class="service-icon"><svg width="36" height="36" viewBox="0 0 36 36" fill="none" stroke="#fff" stroke-width="2.2"><path d="M4 17L18 6l14 11"/><path d="M8 15v15h20V15M13 20h10v10H13zM18 20v10"/></svg></div>
    <div class="service-label" style="margin-top:42px">Screen<br>Rooms</div>
  </div>
  <div class="abs service-item" style="left:110px;top:1063px">
    <div class="service-icon"><svg width="36" height="36" viewBox="0 0 36 36" fill="none" stroke="#fff" stroke-width="2.2"><path d="M4 17L18 6l14 11"/><path d="M8 15v15h20V15M12 20h5v5h-5zM20 20h5v10h-5z"/></svg></div>
    <div class="service-label" style="margin-top:62px">Sunroom</div>
  </div>

  <p class="abs spec-intro">Harlow Gutters &amp; Exteriors specializes<br><span>in the quality installation of:</span></p>
  <div class="abs spec-btn blue" style="left:563px;top:577px;width:238px">Gutter Cleaning and Covers</div>
  <div class="abs spec-btn teal" style="left:809px;top:577px;width:238px">Veltaro Gutter Protection System</div>
  <div class="abs spec-btn teal" style="left:563px;top:631px;width:238px">Patio Covers</div>
  <div class="abs spec-btn blue" style="left:809px;top:631px;width:238px">Seamless Aluminum Gutters &amp; Downspouts</div>

  <h2 class="abs products-title"><b>THE HIGH-QUALITY PRODUCTS</b><br>THAT WE USE:</h2>
  <div class="abs product-card" style="left:567px;top:790px">
    <div class="product-photo" role="img" aria-label="Photo of a white gutter under a grey shingle roof" style="background:linear-gradient(160deg,#6f7378 0%,#8d8f92 55%,#b7a895 100%)"></div>
    <div class="product-name">Gutter</div>
  </div>
  <div class="abs product-card" style="left:813px;top:790px">
    <div class="product-photo" role="img" aria-label="Photo of a brick house with leaf protection on its gutters" style="background:linear-gradient(180deg,#a9c6e6 0%,#c9b8a6 45%,#9d8a78 100%)"></div>
    <div class="product-name">Leaf protection</div>
  </div>
  <div class="abs product-card" style="left:567px;top:948px">
    <div class="product-photo" role="img" aria-label="Photo of a screened porch room on a lawn" style="background:linear-gradient(180deg,#9fc1e4 0%,#d9dde2 45%,#6e9153 100%)"></div>
    <div class="product-name">Screen rooms</div>
  </div>
  <div class="abs product-card" style="left:813px;top:948px">
    <div class="product-photo" role="img" aria-label="Photo of a white sunroom addition with many windows" style="background:linear-gradient(180deg,#b3cbe4 0%,#ece6d8 40%,#6d6a62 70%,#d7cbb5 100%)"></div>
    <div class="product-name">Sunrooms</div>
  </div>
  <p class="abs craft-note"><b>And the quality craftsmanship</b> homeowners will receive when they choose to go with our company.</p>

  <div class="abs band band-years">
    <span>We have <b>over 50 years</b> in the<br>remodeling industry</span>
  </div>
  <svg class="abs" style="left:46px;top:1162px" width="98" height="112" viewBox="0 0 98 112">
    <path d="M49 4l42 14v36c0 28-20 46-42 54C27 100 7 82 7 54V18z" fill="#f2b51d"/>
    <path d="M49 13l33 11v30c0 22-15 37-33 44C31 91 16 76 16 54V24z" fill="#2a2470"/>
    <text x="49" y="58" text-anchor="middle" font-family="Montserrat,sans-serif" font-weight="800" font-size="34" fill="#f2b51d">50</text>
    <text x="49" y="74" text-anchor="middle" font-family="Montserrat,sans-serif" font-weight="600" font-size="10" letter-spacing="2" fill="#fff">YEARS</text>
  </svg>
  <div class="abs band band-area">
    <span>We provide services all of<br><b>Middle Georgia</b></span>
  </div>
  <svg class="abs" style="left:580px;top:1165px" width="56" height="90" viewBox="0 0 56 90">
    <path d="M28 2C13 2 3 14 3 28c0 20 25 58 25 58s25-38 25-58C53 14 43 2 28 2z" fill="#d83a45"/>
    <ellipse cx="28" cy="28" rx="13" ry="15" fill="#fff"/>
  </svg>

  <div class="abs brand-name"><span class="brand-mark"></span><span>HARLOW GUTTERS &amp;<br>EXTERIORS</span></div>
  <h2 class="abs touch-title">Get In Touch <b>With Us!</b></h2>
  <div class="abs touch-rule"></div>
  <div class="abs phone">
    <svg width="26" height="26" viewBox="0 0 28 28"><circle cx="14" cy="14" r="13" fill="#17a797"/><path d="M9 7l3 3-2 2c1 2 3 4 5 5l2-2 3 3-2 3c-5 0-11-6-11-11z" fill="#fff"/></svg>
    <span>478-555-0142</span>
  </div>
  <div class="abs contact-lines">
    <div><svg width="16" height="12" viewBox="0 0 16 12"><rect width="16" height="12" fill="#17a797"/><path d="M0 0l8 6 8-6" stroke="#fff" stroke-width="1.5" fill="none"/></svg>hello@harlowgutterexteriors.com</div>
    <div><svg width="16" height="16" viewBox="0 0 16 16" fill="none" stroke="#17a797" stroke-width="1.6"><circle cx="8" cy="8" r="7"/><path d="M1 8h14M8 1c-3 4-3 10 0 14M8 1c3 4 3 10 0 14"/></svg>www.harlowgutterexteriors.com</div>
  </div>
</main>
</body>
</html>
```